Case Study Template

We would like a template for case studies that we can then use whenever we do a great job for our clients to help future clients understand what we do.

Whilst we could just use the word version provided we feel there is probably opportunity to have a much more professionally designed look feel for the template.

The finished case studies will be printed on glossy and used as sales collateral as well as being posted on the web as part of our web based information.

The template needs to be in MS word or MS powerpoint so that we can easily produce new case studies into the future using the template format.

The attached incorporates the basic structure with the initial section providing some context, then 3 main sections (boxes) for the the actual case study detail.

Very open to different convention if you have experience in this regard.....

Target Market(s)

Small to medium business owners and their advisors (Accountants, Bankers, Consultants)

Industry/Entity Type

Sales

Requirements
Must have
• We need the caption at the bottom referring to Quenby being a holder of Australian Credit License ..... as this is a regulatory requirement.

It must have our logo in the design

```html
<!DOCTYPE html>
<html lang="en">
<head>
<meta charset="utf-8">
<title>Quenby Case Study</title>
<link href="https://fonts.googleapis.com/css2?family=Open+Sans:wght@400;600;700&display=swap" rel="stylesheet">
<style>
  :root {
    --backdrop: #555555;
    --paper: #ffffff;
    --gold: #e6bd55;
    --panel: #efebde;
    --ink: #2b2b2b;
    --muted: #555555;
    --rule: #d9b453;
    --brand: #4a5358;
  }
  * { box-sizing: border-box; margin: 0; padding: 0; }
  html, body { width: 1200px; height: 1000px; overflow: hidden; }
  body { background: var(--backdrop); font-family: "Open Sans", Arial, sans-serif; color: var(--ink); position: relative; }

  .page { position: absolute; left: 358px; top: 158px; width: 483px; height: 683px; background: var(--paper); }

  .brand-name { position: absolute; left: 30px; top: 30px; font-size: 20px; font-weight: 600; line-height: 24px; color: var(--brand); }

  .doc-type { position: absolute; right: 29px; top: 58px; font-size: 6px; letter-spacing: .3px; color: var(--muted); }

  .banner { position: absolute; left: 30px; top: 77px; width: 426px; height: 116px;
    background: linear-gradient(100deg, #8a6a25 0%, #c9a55a 30%, #ead7a6 55%, #c49a45 80%, #7c5d1f 100%); }
  .banner-band { position: absolute; left: 0; top: 22px; width: 426px; height: 76px;
    background: linear-gradient(90deg, rgba(255,250,235,.85) 0%, rgba(255,250,235,.6) 60%, rgba(255,250,235,0) 85%); }
  .banner-title { position: absolute; left: 4px; top: 28px; width: 272px; font-size: 13px; font-weight: 600; line-height: 21px; color: #3a3326; }

  .col-label { position: absolute; left: 29px; top: 206px; width: 136px; }
  .col-main { position: absolute; left: 176px; top: 206px; width: 278px; }

  .section-head { background: var(--gold); font-size: 8.5px; font-weight: 700; color: #3a2f12; padding: 1px 6px; height: 14px; line-height: 12px; }
  .section-body { background: var(--panel); color: var(--ink); }

  .facts .section-body { font-size: 7.5px; line-height: 11.7px; font-weight: 600; padding: 4px 5px 5px; height: 21px; }
  .facts .summary { height: auto; padding: 4px 5px 7px; }

  .detail .section-body { padding: 4px 4px 4px 34px; }
  .detail ul { list-style: disc; }
  .detail li { font-size: 7.3px; line-height: 11px; }

  .footer-rule { position: absolute; left: 24px; top: 634px; width: 435px; height: 1px; background: var(--rule); }
  .footer { position: absolute; left: 29px; top: 642px; font-size: 5.3px; line-height: 8px; color: var(--ink); }
  .footer a { color: #1e4c8f; text-decoration: underline; }
</style>
</head>
<body>
  <article class="page">
    <div class="brand-name">Quenby</div>
    <div class="doc-type">CASE STUDY</div>

    <div class="banner" role="img" aria-label="Photo of gold coins resting on financial charts and papers">
      <div class="banner-band"></div>
      <h1 class="banner-title">Helping businesses to solve bank problems Lowering costs and improving access to funding</h1>
    </div>

    <aside class="col-label facts">
      <div class="section-head">Quenby Service</div>
      <div class="section-body">Finance Restructure</div>
      <div class="section-head">Industry</div>
      <div class="section-body">Furniture Wholesaler</div>
      <div class="section-head">Turnover</div>
      <div class="section-body">$3M</div>
      <div class="section-head">Executive Summary</div>
      <div class="section-body summary">Quenby procures a material increase in cheaper funding for a client unable to find funding themselves</div>
    </aside>

    <section class="col-main detail">
      <div class="section-head">Situation Appraisal</div>
      <div class="section-body">
        <ul>
          <li>Growing business with increasing import requirements.</li>
          <li>Client applied for an increase in funding directly with the house bank and were told further security was required.&nbsp; One Owner/Director already had his home in the security mix and no further security was readily available.</li>
          <li>Norvale Advisory Partner introduced Quenby, who were later engaged to undertake a financial and banking diagnostic/review.</li>
        </ul>
      </div>
      <div class="section-head">Outcomes/Benefits Delivered</div>
      <div class="section-body">
        <ul>
          <li>Post diagnostic, Quenby completed a financing proposal paper and targeted specific financiers.</li>
          <li>Increased offer of facilities received from an alternative financier. 30% increase in Working Capital facilities.</li>
          <li>Release of personal home from the business security negotiated.</li>
          <li>Review of Facility Documentation and refinance effected.</li>
          <li>Additional temporary funding subsequently provided by the new bank.</li>
          <li>Client achieved a financing result well in excess of what they expected due to their relationship with their Accountant (Norvale Advisory!).</li>
        </ul>
      </div>
      <div class="section-head">Future Opportunities</div>
      <div class="section-body">
        <ul>
          <li>No requirement for ongoing Bank Management support required given current CFO ability and reasonably straight forward business reporting.</li>
          <li>Potential for virtual CFO offering upon retirement of CFO/Finance Director.</li>
          <li>Ad hoc catch up with client and Bank to ensure relationship running smoothly and provide assistance when the CFO transition occurs.</li>
        </ul>
      </div>
    </section>

    <div class="footer-rule"></div>
    <footer class="footer">
      <p>Quenby Financial Services Pty Ltd holds Australian Credit License No. 418207.</p>
      <p>To find out more about Quenby Financial Services Pty Ltd visit our website at <a>www.quenbyfinance.com.au</a> or call us on +61 3 9000 4182</p>
    </footer>
  </article>
</body>
</html>
```